Business Card Design

2 cards please: one for toby and one for marguerite
Updates

Reason: nobody used the 2 wine labels i submitted; please work with black, red, yellow, white only, i would love black gloss raise ink on the front? something strong!

Target Market(s)

rugby fans

Industry/Entity Type

Business

Contact Information for Business Card

Tall Oak Wine, www.domainedevarlonge.example, Toby Varlonge, 0671450926, toby@domainedevarlonge.example, Marguerite Varlonge, 0658174203, marguerite@domainedevarlonge.example

Requirements
Must have
• i would like TMV written as a logo on the front in a family crest type design and on the back the 2 wine labels, which are uploaded and nobody used

```html
<!DOCTYPE html>
<html lang="en">
<head>
<meta charset="utf-8">
<title>Tall Oak Wine – Business Card Variations</title>
<link rel="stylesheet" href="https://fonts.googleapis.com/css2?family=Arimo:wght@400;700&family=Tinos:wght@400;700&display=swap">
<style>
  :root {
    --white: #ffffff;
    --black: #111111;
    --red: #d8262f;
    --red-deep: #b3121c;
    --red-soft: #f08a8f;
    --yellow: #f6c81c;
    --yellow-deep: #e8a800;
    --yellow-pale: #fff3b8;
    --yellow-ghost: #f2da7c;
    --edge: #d9d9d9;
  }
  * { box-sizing: border-box; margin: 0; padding: 0; }
  html, body { width: 1200px; height: 776px; overflow: hidden; background: var(--white); }
  .sheet { position: relative; width: 1200px; height: 776px; font-family: "Arimo", Arial, sans-serif; color: var(--black); }
  .sheet-title { position: absolute; left: 41px; top: 12px; font-size: 16px; font-weight: 400; }

  .card { position: absolute; width: 247px; height: 149px; overflow: hidden; }
  .col-1 { left: 41px; } .col-2 { left: 331px; } .col-3 { left: 630px; } .col-4 { left: 919px; }
  .row-1 { top: 44px; } .row-2 { top: 224px; } .row-3 { top: 407px; } .row-4 { top: 583px; }

  /* Monogram lockup */
  .monogram { position: absolute; left: 0; right: 0; top: 60px; text-align: center; font-family: "Tinos", "Times New Roman", serif; color: var(--black); }
  .monogram-letters { font-size: 17px; font-weight: 700; line-height: 1; letter-spacing: 1px; }
  .monogram-tag { font-size: 5.5px; font-weight: 700; margin-top: 3px; }

  .crest { position: absolute; left: 78px; top: 36px; width: 90px; height: 76px; border-radius: 50%; }

  .contact { position: absolute; font-size: 5px; font-weight: 700; line-height: 1.6; color: var(--black); }
  .contact-name { font-family: "Tinos", "Times New Roman", serif; font-weight: 400; font-size: 7px; line-height: 1.3; margin-bottom: 2px; }
  .contact.left { left: 7px; top: 112px; }
  .contact.centered { left: 0; right: 0; top: 57px; text-align: center; }
  .contact.centered .contact-name { font-size: 9px; }

  .domain { position: absolute; font-family: "Tinos", "Times New Roman", serif; font-size: 5px; white-space: nowrap; }

  /* Style A: white with red wave */
  .style-wave { background: var(--white); border: 1px solid var(--edge); }
  .style-wave .wave { position: absolute; left: 0; top: 0; width: 247px; height: 40px; }
  .style-wave .wave path { fill: var(--red); }
  .style-wave .domain { right: 6px; top: 3px; color: var(--white); }
  .style-wave .crest { background: radial-gradient(ellipse, transparent 54%, var(--yellow-pale) 60%, var(--yellow) 68%, var(--yellow-deep) 72%, transparent 80%); }
  .ghost-mark { position: absolute; left: 0; right: 0; top: 66px; text-align: center;
    font-family: "Tinos", "Times New Roman", serif; font-size: 22px; font-weight: 700; letter-spacing: 2px; color: var(--yellow-ghost); }

  /* Style B: white-to-yellow glow with red scrollwork */
  .style-glow { background: radial-gradient(ellipse 55% 60% at 50% 50%, var(--white), var(--yellow-pale) 60%, var(--yellow) 115%); }
  .side-strip { position: absolute; top: 4px; bottom: 4px; width: 6px; border-radius: 3px;
    background: linear-gradient(var(--red), var(--red-soft), var(--red)); }
  .style-glow.front .side-strip { right: 4px; }
  .style-glow.back .side-strip { left: 4px; }
  .style-glow .crest { background: radial-gradient(ellipse, transparent 52%, var(--red-soft) 62%, var(--red) 68%, transparent 78%); }
  .style-glow .contact.left { top: 117px; }
  .style-glow .domain { right: 8px; bottom: 5px; color: var(--yellow-deep); }

  /* Style C: red with yellow frame */
  .style-red { background: var(--red-deep); }
  .frame-line { position: absolute; inset: 7px; border: 1px solid var(--yellow); }
  .corner { position: absolute; width: 16px; height: 16px; border-radius: 50%;
    background: radial-gradient(circle, var(--yellow-pale), var(--yellow) 45%, transparent 75%); }
  .corner.tl { left: 2px; top: 2px; } .corner.tr { right: 2px; top: 2px; }
  .corner.bl { left: 2px; bottom: 2px; } .corner.br { right: 2px; bottom: 2px; }
  .halo { position: absolute; left: 73px; top: 22px; width: 100px; height: 100px; border-radius: 50%;
    background: radial-gradient(circle, var(--white) 34%, var(--red-soft) 58%, transparent 72%); }
  .flourish { position: absolute; left: 98px; width: 50px; height: 14px; border-radius: 50%;
    background: radial-gradient(ellipse, var(--yellow-pale), var(--yellow) 50%, transparent 75%); }
  .flourish.top { top: 36px; } .flourish.bottom { top: 96px; }
  .style-red .domain, .style-yellow .domain { left: 0; right: 0; bottom: 11px; text-align: center; }
  .style-red .domain { color: var(--yellow); }

  /* Style D: yellow with red burst */
  .style-yellow { background: radial-gradient(ellipse 48% 52% at 50% 48%, var(--red), #e8582a 40%, var(--yellow) 82%); }
  .style-yellow.back { background: radial-gradient(ellipse 55% 60% at 50% 50%, var(--yellow-pale), var(--yellow) 80%); }
  .style-yellow .frame-line { border-color: var(--white); }
  .style-yellow .corner { background: radial-gradient(circle, var(--white), var(--yellow-pale) 40%, transparent 75%); }
  .style-yellow .flourish { background: radial-gradient(ellipse, var(--white), var(--yellow-pale) 45%, transparent 75%); }
  .style-yellow.front .monogram { color: var(--white); }
  .style-yellow .domain { color: var(--white); }
</style>
</head>
<body>
<main class="sheet">
  <h1 class="sheet-title">Variations:</h1>

  <!-- Row 1: white with red wave -->
  <section class="card style-wave front col-1 row-1">
    <svg class="wave" viewBox="0 0 247 40" aria-hidden="true"><path d="M0 0H247V6C205 8 175 26 125 22C80 18 35 14 0 30Z"/></svg>
    <span class="domain">www.domainedevarlonge.example</span>
    <div class="crest" role="img" aria-label="Yellow oval family crest filigree frame"></div>
    <div class="monogram"><div class="monogram-letters">TMV</div><div class="monogram-tag">Tall Oak Wine</div></div>
    <div class="contact left"><div class="contact-name">Toby Varlonge</div>Cell: 0671450926<br>toby@domainedevarlonge.example</div>
  </section>
  <section class="card style-wave back col-2 row-1">
    <svg class="wave" viewBox="0 0 247 40" aria-hidden="true"><path d="M0 0H247V6C205 8 175 26 125 22C80 18 35 14 0 30Z"/></svg>
    <div class="ghost-mark">TMV</div>
  </section>
  <section class="card style-wave front col-3 row-1">
    <svg class="wave" viewBox="0 0 247 40" aria-hidden="true"><path d="M0 0H247V6C205 8 175 26 125 22C80 18 35 14 0 30Z"/></svg>
    <span class="domain">www.domainedevarlonge.example</span>
    <div class="crest" role="img" aria-label="Yellow oval family crest filigree frame"></div>
    <div class="monogram"><div class="monogram-letters">TMV</div><div class="monogram-tag">Tall Oak Wine</div></div>
    <div class="contact left"><div class="contact-name">Marguerite Varlonge</div>Cell: 0658174203<br>marguerite@domainedevarlonge.example</div>
  </section>
  <section class="card style-wave back col-4 row-1">
    <svg class="wave" viewBox="0 0 247 40" aria-hidden="true"><path d="M0 0H247V6C205 8 175 26 125 22C80 18 35 14 0 30Z"/></svg>
    <div class="ghost-mark">TMV</div>
  </section>

  <!-- Row 2: white-to-yellow glow -->
  <section class="card style-glow front col-1 row-2">
    <div class="side-strip" role="img" aria-label="Red vertical scroll ornament"></div>
    <div class="crest" role="img" aria-label="Red scrollwork family crest"></div>
    <div class="monogram"><div class="monogram-letters">TMV</div><div class="monogram-tag">Tall Oak Wine</div></div>
    <div class="contact left"><div class="contact-name">Toby Varlonge</div>Cell: 0671450926<br>toby@domainedevarlonge.example</div>
  </section>
  <section class="card style-glow back col-2 row-2">
    <div class="side-strip" role="img" aria-label="Red vertical scroll ornament"></div>
    <span class="domain">www.domainedevarlonge.example</span>
  </section>
  <section class="card style-glow front col-3 row-2">
    <div class="side-strip" role="img" aria-label="Red vertical scroll ornament"></div>
    <div class="crest" role="img" aria-label="Red scrollwork family crest"></div>
    <div class="monogram"><div class="monogram-letters">TMV</div><div class="monogram-tag">Tall Oak Wine</div></div>
    <div class="contact left"><div class="contact-name">Marguerite Varlonge</div>Cell: 0658174203<br>marguerite@domainedevarlonge.example</div>
  </section>
  <section class="card style-glow back col-4 row-2">
    <div class="side-strip" role="img" aria-label="Red vertical scroll ornament"></div>
    <span class="domain">www.domainedevarlonge.example</span>
  </section>

  <!-- Row 3: red with yellow frame -->
  <section class="card style-red front col-1 row-3">
    <div class="frame-line"></div>
    <div class="corner tl" role="img" aria-label="Yellow corner ornament"></div><div class="corner tr" role="img" aria-label="Yellow corner ornament"></div>
    <div class="corner bl" role="img" aria-label="Yellow corner ornament"></div><div class="corner br" role="img" aria-label="Yellow corner ornament"></div>
    <div class="halo"></div>
    <div class="flourish top" role="img" aria-label="Yellow crest crown flourish"></div><div class="flourish bottom" role="img" aria-label="Yellow crest base flourish"></div>
    <div class="monogram"><div class="monogram-letters">TMV</div><div class="monogram-tag">Tall Oak Wine</div></div>
    <span class="domain">www.domainedevarlonge.example</span>
  </section>
  <section class="card style-red back col-2 row-3">
    <div class="frame-line"></div>
    <div class="corner tl" role="img" aria-label="Yellow corner ornament"></div><div class="corner tr" role="img" aria-label="Yellow corner ornament"></div>
    <div class="corner bl" role="img" aria-label="Yellow corner ornament"></div><div class="corner br" role="img" aria-label="Yellow corner ornament"></div>
    <div class="halo"></div>
    <div class="flourish top" role="img" aria-label="Yellow crest crown flourish"></div><div class="flourish bottom" role="img" aria-label="Yellow crest base flourish"></div>
    <div class="contact centered"><div class="contact-name">Toby Varlonge</div>Cell: 0671450926<br>toby@domainedevarlonge.example</div>
  </section>
  <section class="card style-red front col-3 row-3">
    <div class="frame-line"></div>
    <div class="corner tl" role="img" aria-label="Yellow corner ornament"></div><div class="corner tr" role="img" aria-label="Yellow corner ornament"></div>
    <div class="corner bl" role="img" aria-label="Yellow corner ornament"></div><div class="corner br" role="img" aria-label="Yellow corner ornament"></div>
    <div class="halo"></div>
    <div class="flourish top" role="img" aria-label="Yellow crest crown flourish"></div><div class="flourish bottom" role="img" aria-label="Yellow crest base flourish"></div>
    <div class="monogram"><div class="monogram-letters">TMV</div><div class="monogram-tag">Tall Oak Wine</div></div>
    <span class="domain">www.domainedevarlonge.example</span>
  </section>
  <section class="card style-red back col-4 row-3">
    <div class="frame-line"></div>
    <div class="corner tl" role="img" aria-label="Yellow corner ornament"></div><div class="corner tr" role="img" aria-label="Yellow corner ornament"></div>
    <div class="corner bl" role="img" aria-label="Yellow corner ornament"></div><div class="corner br" role="img" aria-label="Yellow corner ornament"></div>
    <div class="halo"></div>
    <div class="flourish top" role="img" aria-label="Yellow crest crown flourish"></div><div class="flourish bottom" role="img" aria-label="Yellow crest base flourish"></div>
    <div class="contact centered"><div class="contact-name">Marguerite Varlonge</div>Cell: 0658174203<br>marguerite@domainedevarlonge.example</div>
  </section>

  <!-- Row 4: yellow with red burst -->
  <section class="card style-yellow front col-1 row-4">
    <div class="frame-line"></div>
    <div class="corner tl" role="img" aria-label="White corner ornament"></div><div class="corner tr" role="img" aria-label="White corner ornament"></div>
    <div class="corner bl" role="img" aria-label="White corner ornament"></div><div class="corner br" role="img" aria-label="White corner ornament"></div>
    <div class="flourish top" role="img" aria-label="White crest crown flourish"></div><div class="flourish bottom" role="img" aria-label="White crest base flourish"></div>
    <div class="monogram"><div class="monogram-letters">TMV</div><div class="monogram-tag">Tall Oak Wine</div></div>
    <span class="domain">www.domainedevarlonge.example</span>
  </section>
  <section class="card style-yellow back col-2 row-4">
    <div class="frame-line"></div>
    <div class="corner tl" role="img" aria-label="White corner ornament"></div><div class="corner tr" role="img" aria-label="White corner ornament"></div>
    <div class="corner bl" role="img" aria-label="White corner ornament"></div><div class="corner br" role="img" aria-label="White corner ornament"></div>
    <div class="flourish top" role="img" aria-label="White crest crown flourish"></div><div class="flourish bottom" role="img" aria-label="White crest base flourish"></div>
    <div class="contact centered"><div class="contact-name">Toby Varlonge</div>Cell: 0671450926<br>toby@domainedevarlonge.example</div>
  </section>
  <section class="card style-yellow front col-3 row-4">
    <div class="frame-line"></div>
    <div class="corner tl" role="img" aria-label="White corner ornament"></div><div class="corner tr" role="img" aria-label="White corner ornament"></div>
    <div class="corner bl" role="img" aria-label="White corner ornament"></div><div class="corner br" role="img" aria-label="White corner ornament"></div>
    <div class="flourish top" role="img" aria-label="White crest crown flourish"></div><div class="flourish bottom" role="img" aria-label="White crest base flourish"></div>
    <div class="monogram"><div class="monogram-letters">TMV</div><div class="monogram-tag">Tall Oak Wine</div></div>
    <span class="domain">www.domainedevarlonge.example</span>
  </section>
  <section class="card style-yellow back col-4 row-4">
    <div class="frame-line"></div>
    <div class="corner tl" role="img" aria-label="White corner ornament"></div><div class="corner tr" role="img" aria-label="White corner ornament"></div>
    <div class="corner bl" role="img" aria-label="White corner ornament"></div><div class="corner br" role="img" aria-label="White corner ornament"></div>
    <div class="flourish top" role="img" aria-label="White crest crown flourish"></div><div class="flourish bottom" role="img" aria-label="White crest base flourish"></div>
    <div class="contact centered"><div class="contact-name">Marguerite Varlonge</div>Cell: 0658174203<br>marguerite@domainedevarlonge.example</div>
  </section>
</main>
</body>
</html>
```